Meadowlark Crate Society - New Website Design

Create a professional website for strawberries of the month club; a subscription box business that will INCLUDE dipped strawberries - some with sprinkles. Check out: http://www.plumvine.com for examples. Our website URL will be www.MeadowlarkCrateSociety.com
Please see quillpouch.com; toffeeguild.com and gruffcase.com for the concept I am after. The business has not been launched yet, I am currently in the pre-launch stage using a specialized landing page website, and so the time scale for developing my professional looking website is up to 1-2 weeks.
The webpage should have a fun feel and should match the style of the company logo at toffeeguild.com or gruffcase.com. The pages to include are 'Home', 'About us' and 'Get Started'
Thank you and good luck!

```html
<!DOCTYPE html>
<html lang="en">
<head>
<meta charset="utf-8">
<title>Meadowlark Crate Society</title>
<link href="https://fonts.googleapis.com/css2?family=Open+Sans:wght@400;600;700&display=swap" rel="stylesheet">
<style>
:root{
  --red:#ef2b2f;
  --ink:#111111;
  --text:#444444;
  --muted:#666666;
  --paper:#ffffff;
  --footer:#f2f2f2;
}
*{box-sizing:border-box;margin:0;padding:0}
html,body{width:693px;height:1200px;overflow:hidden;background:var(--paper)}
body{position:relative;font-family:'Open Sans',Arial,sans-serif;color:var(--text)}
.abs{position:absolute}
.btn{position:absolute;background:var(--red);color:#fff;font-weight:600;display:flex;align-items:center;justify-content:center;border-radius:1px;white-space:nowrap}

.site-header{position:absolute;left:0;top:0;width:693px;height:47px;background:var(--paper)}
.brand{left:56px;top:11px;font-size:17px;font-weight:700;color:var(--red);white-space:nowrap}
.nav-link{top:17px;font-size:8.5px;color:var(--muted);white-space:nowrap}
.nav-cta{left:577px;top:14px;width:59px;height:19px;font-size:8px}

.hero{position:absolute;left:0;top:47px;width:693px;height:293px;overflow:hidden;
  background:linear-gradient(90deg,#d9cfc8 0%,#efe9e6 40%,#f4dede 60%,#f0c9c8 100%)}
.hero-photo{position:absolute;left:40px;top:0;width:300px;height:293px;background:linear-gradient(180deg,#b8a89c,#9fb0c4 60%,#d9d4cf)}
.hero-fruit{position:absolute;left:270px;top:0;width:423px;height:293px;background:radial-gradient(ellipse at 60% 40%,#f0a7a5 0%,#f4cfcd 55%,rgba(244,223,222,0) 80%)}
.hero-title{left:327px;top:145px;width:300px;font-size:24px;line-height:28px;font-weight:700;color:var(--ink)}
.hero-rule{left:452px;top:190px;width:163px;height:1px;background:var(--red)}
.hero-sub{left:329px;top:203px;font-size:10.5px;font-weight:600;color:var(--ink);white-space:nowrap}
.hero-cta{left:327px;top:228px;width:116px;height:28px;font-size:12px}
.hero-offer{left:454px;top:224px;font-size:29px;line-height:36px;font-weight:700;color:var(--red);white-space:nowrap}
.dots{left:326px;top:313px;display:flex;gap:4px}
.dots span{width:7px;height:7px;border-radius:50%;background:#888}
.dots span.on{background:var(--red)}

.section-title{position:absolute;left:0;width:693px;text-align:center;font-size:17px;font-weight:700;color:var(--red)}
.step{position:absolute;top:421px;width:150px;text-align:center}
.step svg{display:block;margin:0 auto}
.step h3{margin-top:12px;font-size:9.5px;font-weight:700;color:var(--red);line-height:12px;height:24px}
.step p{margin-top:6px;font-size:6.3px;line-height:12px;color:var(--text)}
.steps-cta{left:288px;top:580px;width:117px;height:23px;font-size:12.5px}

.plan{position:absolute;top:703px;width:150px;height:234px;border:1.5px solid var(--red);text-align:center;padding-top:31px}
.plan-photo{position:absolute;top:659px;width:64px;height:64px;border-radius:50%;border:1.5px solid var(--red);background:#fff;padding:3px}
.plan-photo div{width:100%;height:100%;border-radius:50%}
.plan h3{font-size:13.5px;font-weight:700;color:#333}
.plan .pack{font-size:8px;font-weight:600;color:#444;margin-top:1px}
.plan .price{font-size:12px;font-weight:700;color:#333;margin-top:4px}
.plan ul{list-style:none;margin-top:9px}
.plan li{font-size:8.5px;color:#555;height:24px;line-height:24px}
.plan .btn{left:35px;top:194px;width:80px;height:21px;font-size:9px}

.newsletter{position:absolute;left:0;top:963px;width:693px;height:81px;overflow:hidden;
  background:linear-gradient(90deg,#f1ebe8,#e9dcd6 45%,#efe3df 70%,#f2ece9)}
.news-label{left:149px;top:994px;font-size:13px;font-weight:700;color:var(--red);white-space:nowrap}
.news-input{left:296px;top:993px;width:177px;height:20px;background:#fff;font-size:7px;color:#333;padding:6px 11px}
.news-btn{left:484px;top:992px;width:79px;height:21px;font-size:9px}

.site-footer{position:absolute;left:0;top:1044px;width:693px;height:156px;background:var(--footer)}
.foot-col{top:1083px;font-size:8px;line-height:14.8px;color:#333;list-style:none;white-space:nowrap}
.foot-brand{left:409px;top:1069px;font-size:15.5px;font-weight:700;color:var(--red);white-space:nowrap}
.social{top:1104px;width:27px;height:27px;background:var(--red)}
.crate{left:0;top:1110px;width:100px;height:88px;background:linear-gradient(135deg,#c9333a,#a51e2a 60%,#d8d0c8)}
.copyright{left:0;top:1173px;width:693px;text-align:center;font-size:6.5px;color:#333}
</style>
</head>
<body>

<header class="site-header">
  <div class="abs brand">Meadowlark Crate Society</div>
  <a class="abs nav-link" style="left:491px">Home</a>
  <a class="abs nav-link" style="left:532px">About Us</a>
  <a class="btn nav-cta">Get started</a>
</header>

<section class="hero">
  <div class="hero-fruit" role="img" aria-label="Large fresh strawberries on a white plate"></div>
  <div class="hero-photo" role="img" aria-label="Smiling couple sharing a strawberry"></div>
</section>
<h1 class="abs hero-title">Monthly Subscription for Loved One</h1>
<div class="abs hero-rule"></div>
<div class="abs hero-sub">to giving them delicious &amp; healthy Fruit</div>
<a class="btn hero-cta">Subscribe Now</a>
<div class="abs hero-offer">50% Offer</div>
<div class="abs dots"><span></span><span></span><span class="on"></span><span></span></div>

<h2 class="section-title" style="top:365px">How it Works</h2>

<div class="step" style="left:104px">
  <svg width="50" height="50" viewBox="0 0 50 50"><circle cx="25" cy="25" r="23.5" fill="none" stroke="var(--red)" stroke-width="1.5"/><circle cx="25" cy="25" r="20" fill="var(--red)"/><text x="25" y="30.5" text-anchor="middle" font-family="Open Sans, sans-serif" font-size="15" font-weight="700" fill="#fff">01</text></svg>
  <h3>Choose Month</h3>
  <p>Lorem ipsum dolor sit amet, consectetur adipiscing elit, sed do eiusmod tempor incididunt ut labore et dolore magna aliqua. Ut enim ad minim veniam,</p>
</div>
<div class="step" style="left:272px">
  <svg width="50" height="50" viewBox="0 0 50 50"><circle cx="25" cy="25" r="23.5" fill="none" stroke="var(--red)" stroke-width="1.5"/><circle cx="25" cy="25" r="20" fill="var(--red)"/><text x="25" y="30.5" text-anchor="middle" font-family="Open Sans, sans-serif" font-size="15" font-weight="700" fill="#fff">02</text></svg>
  <h3>Select Package</h3>
  <p>Lorem ipsum dolor sit amet, consectetur adipiscing elit, sed do eiusmod tempor incididunt ut labore et dolore magna aliqua. Ut enim ad minim veniam,</p>
</div>
<div class="step" style="left:439px">
  <svg width="50" height="50" viewBox="0 0 50 50"><circle cx="25" cy="25" r="23.5" fill="none" stroke="var(--red)" stroke-width="1.5"/><circle cx="25" cy="25" r="20" fill="var(--red)"/><text x="25" y="30.5" text-anchor="middle" font-family="Open Sans, sans-serif" font-size="15" font-weight="700" fill="#fff">03</text></svg>
  <h3>Deliver your<br>subscription box</h3>
  <p>Lorem ipsum dolor sit amet, consectetur adipiscing elit, sed do eiusmod tempor incididunt ut labore et dolore magna aliqua. Ut enim ad minim veniam,</p>
</div>

<a class="btn steps-cta">Get Started</a>

<h2 class="section-title" style="top:622px">Our Subscription&nbsp; Plans</h2>

<div class="plan" style="left:107px">
  <h3>Monthly Plan</h3><div class="pack">Small Pack</div><div class="price">$ 29.99 / Month</div>
  <ul><li>Lorium ipsum</li><li>Dolor Amit</li><li>Sit amit</li><li>Lorium Dolor</li></ul>
  <a class="btn">Get Started</a>
</div>
<div class="plan" style="left:271px">
  <h3>6Month Plan</h3><div class="pack">Medium Pack</div><div class="price">$ 34.99 / Month</div>
  <ul><li>Lorium ipsum</li><li>Dolor Amit</li><li>Sit amit</li><li>Lorium Dolor</li></ul>
  <a class="btn">Get Started</a>
</div>
<div class="plan" style="left:436px">
  <h3>12Month Plan</h3><div class="pack">Large Pack</div><div class="price">$ 45.99 / Month</div>
  <ul><li>Lorium ipsum</li><li>Dolor Amit</li><li>Sit amit</li><li>Lorium Dolor</li></ul>
  <a class="btn">Get Started</a>
</div>
<div class="plan-photo" style="left:150px"><div role="img" aria-label="Gift bag of strawberries tied with a ribbon" style="background:radial-gradient(circle,#e2333a 0%,#f08a8c 55%,#f3f0ef 85%)"></div></div>
<div class="plan-photo" style="left:314px"><div role="img" aria-label="Chocolate dipped strawberries" style="background:radial-gradient(circle,#5a2e22 0%,#8a4b3a 45%,#c94a44 75%,#f1e6e4 95%)"></div></div>
<div class="plan-photo" style="left:479px"><div role="img" aria-label="Box of fresh strawberries" style="background:radial-gradient(circle,#d9262c 0%,#e8464a 55%,#f6dede 90%)"></div></div>

<section class="newsletter" role="img" aria-label="Soft background of a woman biting a strawberry"></section>
<div class="abs news-label">Newsletter Subscribe</div>
<div class="abs news-input">Enter Email
  <svg class="abs" style="right:8px;top:6px" width="8" height="7" viewBox="0 0 8 7"><rect x="0.5" y="0.5" width="7" height="6" fill="none" stroke="#333" stroke-width="0.9"/><path d="M0.5 0.8 L4 3.8 L7.5 0.8" fill="none" stroke="#333" stroke-width="0.9"/></svg>
</div>
<a class="btn news-btn">Subscribe</a>

<footer class="site-footer"></footer>
<ul class="abs foot-col" style="left:121px"><li>About Meadowlark Crate</li><li>Monthly Plan</li><li>Billing</li><li>Account Info</li></ul>
<ul class="abs foot-col" style="left:274px"><li>Charity</li><li>FAQ</li><li>Privacy Policy</li><li>Terms of Service</li></ul>
<div class="abs foot-brand">Meadowlark Crate Society</div>
<div class="abs social" style="left:413px" aria-label="Social link"></div>
<div class="abs social" style="left:448px" aria-label="Social link"></div>
<div class="abs social" style="left:483px" aria-label="Social link"></div>
<div class="abs social" style="left:518px" aria-label="Social link"></div>
<div class="abs crate" role="img" aria-label="Wooden crate full of strawberries"></div>
<div class="abs copyright">© 2017 www.companyname.com &nbsp;|&nbsp; All Rights Reserved</div>

</body>
</html>
```